Brontello Pizza Website

We are working with Brontello Pizza and designing them a website.

Some sites to use for content/competitors and inspiration:

https://marvettis.example
https://www.tqz.example
https://brightolives.example/en-us/

Thank you for taking the time to consider designing a website for us. We are web developers based in Stockton, CA, USA. Most of our projects go through the same process. Understanding this process may help you win a project with us. We custom-code all of our websites in-house. We don’t have any requirements as to what tools you use for your design, but we prefer Figma files. For any design that we label as four-stars, we send it to the client for review. The client picks the final design they want us to use. Once we complete this process, we will continue to show additional clients all the four-star sites and purchase them later. Your designs will have multiple chances to sell. For better chances of success, we ask that you follow these guidelines.

IMAGES:
If you use any images or icons in the design, we ask that you have a link to the asset so we can purchase the image/icon. Most of the designs we submit do not have the customer’s images on them unless they have some great images. Be creative; show us the feeling you are trying to portray with your image choices. Use any royalty-free site you choose. We subscribe to Corvane and mainly use their images, but we can purchase images outside of Corvane.

PLEASE NOTE: we will not submit designs to clients with watermarks on the images.

FONTS:
We ask that you identify the fonts used in the design. This can be done in a message if you want. We typically use Plinster Fonts and Corvane Fonts.

CONTENT:
We're always open to different content and ideas. We often submit designs with stock images so the client can see our vision. We typically take pictures after the website launch to use their images with our vision. Lorem Ipsum is fine for paragraphs, but we ask that you write the headers in correct English. We want to be able to show the vision and identify the sections of the website.

INSPIRATION:
We typically add a couple of links in the brief of websites we like to help you get started in your design.

REVISIONS:
We do not often ask for revisions of the designs unless we see something in the design that may not appeal to the client. If there are slight changes that we want to make, we do that in the development process.

FEEDBACK:
We rarely give feedback on designs during the design process. We are working on many website projects and do not have the time to provide feedback. We usually respond if your request is well thought out and asks specific questions, but a note asking “feedback, please” usually goes unanswered.

```html
<!DOCTYPE html>
<html lang="en">
<head>
<meta charset="utf-8">
<title>Brontello Pizza</title>
<link rel="stylesheet" href="https://fonts.googleapis.com/css2?family=Fira+Sans+Condensed:wght@300;400;500;600&family=Poppins:wght@400;500;600;700&display=swap">
<style>
  :root {
    --red: #e52d2d;
    --red-btn: #e8372f;
    --green: #3bb54a;
    --ink: #1d1d1d;
    --grey: #555;
    --black: #0d0d0d;
    --white: #ffffff;
    --line: #e4e4e4;
  }
  * { box-sizing: border-box; margin: 0; padding: 0; }
  html, body { width: 1200px; height: 4528px; overflow: hidden; background: var(--white); }
  body { position: relative; font-family: "Poppins", sans-serif; color: var(--ink); }
  .abs { position: absolute; }
  .btn {
    position: absolute; display: flex; align-items: center; justify-content: center;
    color: var(--white); border-radius: 30px; font-family: "Poppins", sans-serif; text-transform: uppercase; font-weight: 400;
  }
  .btn-red { background: var(--red-btn); }
  .btn-green { background: var(--green); box-shadow: 0 0 14px rgba(59,181,74,.6); }
  .photo { position: absolute; }

  /* Header */
  .header { position: absolute; left: 0; top: 0; width: 1200px; height: 93px; background: var(--white); }
  .header .rule { position: absolute; left: 63px; right: 63px; top: 92px; height: 1px; background: var(--line); }
  .header .pill { top: 9px; height: 33px; font-size: 12px; font-weight: 500; }
  .nav { position: absolute; top: 66px; font-size: 13px; font-weight: 500; text-transform: uppercase; color: #222; }
  .brand-flag {
    position: absolute; left: 540px; top: 0; width: 160px; height: 178px; background: var(--white);
    clip-path: polygon(0 0, 100% 0, 100% 62%, 50% 100%, 0 62%); z-index: 5;
    display: flex; flex-direction: column; align-items: center; padding-top: 34px;
  }
  .brand-dot { width: 26px; height: 26px; border-radius: 50%; background: var(--red); margin-bottom: 8px; }
  .brand-name { font-family: "Fira Sans Condensed", sans-serif; font-weight: 600; font-size: 30px; color: var(--ink); letter-spacing: 1px; }

  /* Hero */
  .hero-photo { left: 0; top: 93px; width: 1200px; height: 879px;
    background: radial-gradient(ellipse at 60% 45%, #e9b36a 0%, #d99a52 35%, #c9a683 60%, #e8e3dc 100%); }
  .hero-glass {
    position: absolute; left: 307px; top: 318px; width: 587px; height: 378px; border-radius: 22px;
    background: rgba(255,255,255,.35);
    text-align: center; font-family: "Fira Sans Condensed", sans-serif; color: #1a1a1a;
  }
  .hero-glass .l1 { position: absolute; left: 0; right: 0; top: 90px; font-size: 47px; font-weight: 400; letter-spacing: 1px; }
  .hero-glass .l2 { position: absolute; left: 0; right: 0; top: 144px; font-size: 51px; font-weight: 400; letter-spacing: 3px; }

  /* Promo band */
  .promo { left: 0; top: 972px; width: 1200px; height: 497px; background: var(--red); overflow: hidden; }
  .promo-photo { left: 0; top: 0; width: 540px; height: 497px;
    background: radial-gradient(circle at 30% 45%, #f3d9a0 0%, #e3b26b 45%, #b9763d 80%);
    clip-path: ellipse(100% 80% at 0% 50%); }
  .promo-text { position: absolute; left: 500px; width: 660px; text-align: center; color: var(--white); }

  /* Section titles */
  .title { position: absolute; left: 0; width: 1200px; text-align: center; font-family: "Fira Sans Condensed", sans-serif; font-weight: 400; font-size: 50px; letter-spacing: 3px; color: var(--ink); }
  .title-dot { position: absolute; left: 587px; width: 26px; height: 26px; border-radius: 50%; background: var(--red); }

  /* Menu circles */
  .menu-item { position: absolute; top: 1760px; width: 260px; text-align: center; }
  .menu-ring { position: relative; width: 250px; height: 250px; margin: 0 auto; }
  .menu-ring svg { position: absolute; left: 0; top: 0; width: 250px; height: 250px; }
  .menu-ring .dish { position: absolute; left: 11px; top: 11px; width: 228px; height: 228px; border-radius: 50%; }
  .menu-label { margin-top: 20px; font-size: 20px; color: #222; }

  /* Delivery banner */
  .delivery { left: 63px; top: 2275px; width: 1072px; height: 520px; border-radius: 24px; overflow: hidden;
    background: linear-gradient(90deg, #f1f1ef 0%, #e4e3df 45%, #d8b480 70%, #c98a45 100%); }
  .delivery h3 { position: absolute; left: 37px; top: 125px; font-family: "Fira Sans Condensed", sans-serif; font-weight: 600; font-size: 40px; letter-spacing: 1px; color: var(--red); }
  .delivery h2 { position: absolute; left: 39px; top: 174px; font-size: 36px; font-weight: 600; color: var(--ink); }
  .delivery p { position: absolute; left: 39px; top: 244px; width: 420px; font-size: 20px; line-height: 29px; color: #333; }

  /* Specials */
  .card { position: absolute; top: 3094px; width: 256px; height: 420px; border: 1px solid #eee; background: var(--white); text-align: center; }
  .card .shot { position: absolute; left: 7px; top: 7px; width: 242px; height: 241px;
    background: radial-gradient(circle at 50% 62%, #d5533a 0%, #c9693f 25%, #c9a07a 45%, #e6d3bd 70%, #f5f1ec 100%); }
  .card .name { position: absolute; left: 0; right: 0; top: 272px; font-size: 18px; font-weight: 600; color: var(--ink); }
  .card .price { position: absolute; left: 0; right: 0; top: 306px; font-size: 17px; font-weight: 600; color: var(--green); }
  .card .btn { left: 72px; top: 348px; width: 112px; height: 34px; font-size: 12px; }

  /* Offer */
  .offer-band { left: 0; top: 3799px; width: 1200px; height: 418px; background: var(--red); }
  .offer-photo { left: 0; top: 3646px; width: 676px; height: 571px;
    background: linear-gradient(180deg, #f7f7f7 0%, #ece2d3 40%, #d8b488 70%, #c94a32 100%); }
  .offer-title { position: absolute; left: 700px; width: 430px; top: 3885px; text-align: center; color: var(--white); font-family: "Fira Sans Condensed", sans-serif; font-weight: 300; font-size: 50px; line-height: 60px; }
  .subscribe { position: absolute; left: 703px; top: 4050px; width: 430px; height: 56px; border: 1.5px solid var(--white); border-radius: 30px; }
  .subscribe span { position: absolute; left: 28px; top: 17px; font-size: 15px; color: var(--white); }
  .subscribe .btn { right: 6px; top: 6px; width: 122px; height: 42px; font-size: 14px; box-shadow: none; }

  /* Footer */
  .footer { position: absolute; left: 0; top: 4217px; width: 1200px; height: 311px; background: var(--black); color: var(--white); }
  .foot-head { position: absolute; top: 70px; font-family: "Fira Sans Condensed", sans-serif; font-weight: 500; font-size: 21px; letter-spacing: 2px; color: var(--white); }
  .foot-rule { position: absolute; top: 105px; width: 30px; height: 2px; background: var(--red); }
  .links { position: absolute; left: 258px; top: 133px; list-style: none; font-size: 14px; color: var(--white); }
  .links li { height: 24px; display: flex; align-items: center; gap: 10px; }
  .contact { position: absolute; left: 745px; font-size: 14px; line-height: 17px; display: flex; gap: 16px; color: var(--white); }
  .contact .ico { width: 22px; height: 22px; border-radius: 4px; background: var(--red); display: flex; align-items: center; justify-content: center; flex: none; }
  .foot-brand { position: absolute; left: 450px; top: 83px; width: 200px; text-align: center; }
  .foot-brand .dot { width: 30px; height: 30px; border-radius: 50%; background: var(--red); margin: 0 auto 12px; }
  .foot-brand .name { font-family: "Fira Sans Condensed", sans-serif; font-weight: 600; font-size: 34px; color: var(--white); letter-spacing: 1px; }
  .copyright { position: absolute; left: 0; width: 1200px; top: 278px; text-align: center; font-size: 12px; color: #ddd; }
</style>
</head>
<body>

<header class="header">
  <div class="btn btn-red pill" style="left:188px;width:148px;">Today's Deal</div>
  <div class="btn btn-red pill" style="left:874px;width:150px;">Delivery &amp; Pick Up</div>
  <span class="nav" style="left:166px;">Home</span>
  <span class="nav" style="left:255px;">Menu</span>
  <span class="nav" style="left:340px;">Catering</span>
  <span class="nav" style="left:744px;">About Us</span>
  <span class="nav" style="left:856px;">Franchise</span>
  <span class="nav" style="left:975px;">Start Your Order</span>
  <div class="rule"></div>
</header>
<div class="brand-flag">
  <div class="brand-dot"></div>
  <div class="brand-name">BRONTELLO</div>
</div>

<div class="photo hero-photo" role="img" aria-label="Close-up of a sliced Italian pizza on a wooden board"></div>
<section class="hero-glass">
  <div class="l1">Fall in love with delicious</div>
  <div class="l2">ITALIAN FRESH PIZZA</div>
  <div class="btn btn-red" style="left:190px;top:232px;width:200px;height:46px;font-size:18px;">Order Now</div>
</section>

<section class="abs promo">
  <div class="photo promo-photo" role="img" aria-label="Stuffed crust pizza topped with peppers and onions"></div>
  <div class="promo-text" style="top:103px;font-size:31px;">LOWEST PRICE ON</div>
  <div class="promo-text" style="top:153px;font-size:58px;font-weight:700;left:480px;width:700px;">STUFFED CRUST PIZZA</div>
  <div class="promo-text" style="top:240px;font-size:20px;line-height:35px;">Lorem ipsum dolor sit amet, consectetur adipiscing elit, sed<br>do eiusmod tempor incididunt ut labore et dolore magna</div>
  <div class="btn btn-green" style="left:722px;top:355px;width:218px;height:58px;font-size:21px;">Order Now</div>
</section>

<div class="title-dot" style="top:1590px;"></div>
<h2 class="title" style="top:1622px;">OUR MENUS</h2>

<div class="menu-item" style="left:54px;">
  <div class="menu-ring">
    <svg viewBox="0 0 250 250"><path d="M38.7 38.7 A122 122 0 0 1 211.3 38.7 M38.7 211.3 A122 122 0 0 0 211.3 211.3" fill="none" stroke="#222" stroke-width="2"/></svg>
    <div class="dish" role="img" aria-label="Vegetable pizza" style="background:radial-gradient(circle,#f0c060 0%,#e09a40 60%,#c77a30 100%);"></div>
  </div>
  <div class="menu-label">VEG PIZZA</div>
</div>
<div class="menu-item" style="left:322px;">
  <div class="menu-ring">
    <svg viewBox="0 0 250 250"><path d="M38.7 38.7 A122 122 0 0 1 211.3 38.7 M38.7 211.3 A122 122 0 0 0 211.3 211.3" fill="none" stroke="#222" stroke-width="2"/></svg>
    <div class="dish" role="img" aria-label="Meat pizza" style="background:radial-gradient(circle,#d9a050 0%,#a8683a 60%,#8a5a30 100%);"></div>
  </div>
  <div class="menu-label">NON-VEG PIZZA</div>
</div>
<div class="menu-item" style="left:594px;">
  <div class="menu-ring">
    <svg viewBox="0 0 250 250"><path d="M38.7 38.7 A122 122 0 0 1 211.3 38.7 M38.7 211.3 A122 122 0 0 0 211.3 211.3" fill="none" stroke="#222" stroke-width="2"/></svg>
    <div class="dish" role="img" aria-label="Burgers with fresh salad" style="background:radial-gradient(circle,#7aa84a 0%,#c44a35 50%,#3a3a2a 100%);"></div>
  </div>
  <div class="menu-label">BURGER PIZZA</div>
</div>
<div class="menu-item" style="left:870px;">
  <div class="menu-ring">
    <svg viewBox="0 0 250 250"><path d="M38.7 38.7 A122 122 0 0 1 211.3 38.7 M38.7 211.3 A122 122 0 0 0 211.3 211.3" fill="none" stroke="#222" stroke-width="2"/></svg>
    <div class="dish" role="img" aria-label="Pizza with grilled vegetables" style="background:radial-gradient(circle,#e8a060 0%,#d0703f 60%,#a05a35 100%);"></div>
  </div>
  <div class="menu-label">FRIED PIZZA</div>
</div>

<div class="btn btn-red" style="left:495px;top:2124px;width:210px;height:50px;font-size:18px;">View All Menus</div>

<section class="abs delivery" role="img" aria-label="Fresh pizza with cherry tomatoes and basil on a wooden board">
  <h3>BRONTELLO ITALIAN PIZZA</h3>
  <h2>Delivery&nbsp; Now Available</h2>
  <p>Lorem ipsum dolor sit amet, consectetur adipiscing elit, sed do eiusmod tempor</p>
  <div class="btn btn-green" style="left:44px;top:359px;width:179px;height:46px;font-size:20px;box-shadow:none;">Order Now</div>
</section>

<div class="title-dot" style="top:2918px;"></div>
<h2 class="title" style="top:2950px;">BRONTELLO SPECIALS</h2>

<article class="card" style="left:61px;">
  <div class="shot" role="img" aria-label="Pizza in an open box"></div>
  <div class="name">2 - PIZZA PACK</div><div class="price">$86.90</div>
  <div class="btn btn-red">Order Now</div>
</article>
<article class="card" style="left:332px;">
  <div class="shot" role="img" aria-label="Pizza on stacked boxes"></div>
  <div class="name">3- PIZZA PACK</div><div class="price">$109.99</div>
  <div class="btn btn-red">Order Now</div>
</article>
<article class="card" style="left:603px;">
  <div class="shot" role="img" aria-label="Pizza on stacked boxes"></div>
  <div class="name">4 - PIZZA PACK</div><div class="price">$86.90</div>
  <div class="btn btn-red">Order Now</div>
</article>
<article class="card" style="left:874px;">
  <div class="shot" role="img" aria-label="Stack of pizza boxes"></div>
  <div class="name">5 - PIZZA PACK</div><div class="price">$86.90</div>
  <div class="btn btn-red">Order Now</div>
</article>

<div class="abs offer-band"></div>
<div class="photo offer-photo" role="img" aria-label="Delivery person in red cap holding an open pizza box"></div>
<h2 class="offer-title">GET 10% OFF YOUR<br>NEXT ORDER</h2>
<div class="subscribe">
  <span>Enter Your Email Address</span>
  <div class="btn btn-green">Subscribe</div>
</div>

<footer class="footer">
  <h4 class="foot-head" style="left:258px;">QUICK LINKS</h4>
  <div class="foot-rule" style="left:258px;"></div>
  <ul class="links">
    <li><svg width="10" height="10"><circle cx="5" cy="5" r="4" fill="#3bb54a"/></svg>Menu</li>
    <li><svg width="10" height="10"><circle cx="5" cy="5" r="4" fill="#3bb54a"/></svg>Catering</li>
    <li><svg width="10" height="10"><circle cx="5" cy="5" r="4" fill="#3bb54a"/></svg>About us</li>
    <li><svg width="10" height="10"><circle cx="5" cy="5" r="4" fill="#3bb54a"/></svg>Franchise</li>
    <li><svg width="10" height="10"><circle cx="5" cy="5" r="4" fill="#3bb54a"/></svg>Start your order</li>
  </ul>
  <div class="foot-brand">
    <div class="dot"></div>
    <div class="name">BRONTELLO</div>
  </div>
  <h4 class="foot-head" style="left:745px;">CONTACT US</h4>
  <div class="foot-rule" style="left:745px;"></div>
  <div class="contact" style="top:135px;">
    <div class="ico"><svg width="12" height="12" viewBox="0 0 24 24"><path d="M6 2l4 5-2 3c1 3 3 5 6 6l3-2 5 4-3 4C10 21 3 14 2 5z" fill="#fff"/></svg></div>
    <div>CALL US<br>8012 555 0147</div>
  </div>
  <div class="contact" style="top:188px;">
    <div class="ico"><svg width="12" height="10" viewBox="0 0 24 18"><rect x="1" y="1" width="22" height="16" fill="#fff"/><path d="M1 1l11 9 11-9" stroke="#e52d2d" stroke-width="2" fill="none"/></svg></div>
    <div>EMAIL US<br>hello@brontello.example</div>
  </div>
  <div class="contact" style="top:241px;">
    <div class="ico"><svg width="10" height="13" viewBox="0 0 20 26"><path d="M10 0a10 10 0 0 1 10 10c0 7-10 16-10 16S0 17 0 10A10 10 0 0 1 10 0z" fill="#fff"/><circle cx="10" cy="10" r="4" fill="#e52d2d"/></svg></div>
    <div>Address Line Dummy here<br>Address line dummy</div>
  </div>
  <div class="copyright">Copyright © 2025 All Rights Reserved By Company name</div>
</footer>

</body>
</html>
```